New Coffee Brand Packaging Design

We need a package design for our new coffee brand called Brindle Oak Coffee. Our brand mission will be displayed on the packaging (along the side or the back) and we currently have a logo that should be displayed on the front. Feel free to suggest a new logo design as you are designing the packaging if it doesn't fit with your vision. The final design should be creative and conservative. We like coffee colors (dark and light browns, white, cream, black, gold). We also like chalkboard art imagery (i.e. coffee cups, theme words from our mission, people, etc.). One famous person from Westbrook Hollow, KY is Terrence Vogt (world famous boxer and activist). If there is a way to draw his image in more of an abstract way where it doesn't infringe any patents that would be the sort of creativity we would like in the packaging. Our coffee brand prides itself on being a coffee for the people. For the average joe, working American who enjoys a good cup of coffee and a good atmosphere.

Brindle Oak Coffee Mission: "We aim to be a coffee company for the people. The people who have an appreciation and love for family, community and who never forget where they came from. Our coffee was born out of Westbrook Hollow, KY…a place like many others where the hearts, the minds and the wills are strong. We hope you enjoy each and every cup. Peace & Blessings."

Requirements
Must have
• (On the side or on the back of the packaging) Brindle Oak Coffee Mission: "We aim to be a coffee company for the people. The people who have an appreciation and love for family, community and who never forget where they came from. Our coffee was born out of Westbrook Hollow, KY…a place like many others where the hearts, the minds and the wills are strong. We hope you enjoy each and every cup. Peace & Blessings."
Nice to have
• Coffee Colors: dark and light browns, white, cream, black, gold

```html
<!DOCTYPE html>
<html lang="en">
<head>
<meta charset="utf-8">
<title>Brindle Oak Coffee – Bag Front</title>
<link href="https://fonts.googleapis.com/css2?family=Delius&family=Bree+Serif&display=swap" rel="stylesheet">
<style>
  :root {
    --roast-dark: #140805;
    --roast-deep: #080302;
    --roast-glow: #1d0c07;
    --cream: #f7e2c4;
    --gold: #e3b334;
    --ink: #1a0d07;
  }
  html, body {
    margin: 0;
    padding: 0;
    width: 750px;
    height: 1200px;
    overflow: hidden;
    background: var(--roast-dark);
  }
  .bag-front {
    position: relative;
    width: 750px;
    height: 1200px;
    overflow: hidden;
    background: var(--roast-dark);
    font-family: "Delius", cursive;
    color: var(--cream);
  }
  .bean-backdrop {
    position: absolute;
    left: 30px;
    top: 250px;
    width: 760px;
    height: 1000px;
    border-radius: 50% 50% 45% 55% / 40% 45% 55% 60%;
    transform: rotate(-28deg);
    background: radial-gradient(ellipse at 45% 45%, var(--roast-deep) 0%, var(--roast-deep) 55%, var(--roast-glow) 75%, var(--roast-dark) 100%);
  }
  .brand-name {
    position: absolute;
    left: 0;
    width: 750px;
    top: 500px;
    margin: 0;
    text-align: center;
    font-family: "Delius", cursive;
    font-weight: 400;
    font-size: 92px;
    line-height: 1;
    color: var(--cream);
  }
  .brand-descriptor {
    position: absolute;
    left: 0;
    width: 750px;
    top: 696px;
    margin: 0;
    text-align: center;
    font-size: 36px;
    letter-spacing: 2px;
    line-height: 1;
    color: var(--cream);
  }
  .weight-badge {
    position: absolute;
    left: 322px;
    top: 820px;
    width: 104px;
    height: 112px;
  }
  .weight-badge svg {
    position: absolute;
    inset: 0;
  }
  .weight-label {
    position: absolute;
    left: 0;
    width: 104px;
    top: 38px;
    text-align: center;
    font-family: "Bree Serif", serif;
    font-size: 32px;
    line-height: 1;
    color: var(--ink);
  }
  .weight-label sup {
    font-size: 17px;
    vertical-align: 11px;
    margin-left: 1px;
  }
  .origin-line {
    position: absolute;
    left: 0;
    width: 750px;
    top: 1090px;
    margin: 0;
    text-align: center;
    font-size: 15px;
    letter-spacing: 0.5px;
    color: var(--cream);
  }
</style>
</head>
<body>
  <main class="bag-front">
    <div class="bean-backdrop" role="img" aria-label="Large faint coffee bean decoration behind the label"></div>

    <h1 class="brand-name">Brindle Oak</h1>
    <p class="brand-descriptor">COFFEE</p>

    <div class="weight-badge">
      <svg viewBox="0 0 104 112" width="104" height="112" aria-hidden="true">
        <polygon points="52,2 100,28 100,84 52,110 4,84 4,28" fill="var(--ink)" stroke="var(--gold)" stroke-width="2" stroke-linejoin="round"/>
        <polygon points="52,8 95,31 95,81 52,104 9,81 9,31" fill="var(--gold)" stroke-linejoin="round"/>
      </svg>
      <div class="weight-label">12<sup>OZ</sup></div>
    </div>

    <p class="origin-line">WESTBROOK HOLLOW - KY • USA</p>
  </main>
</body>
</html>
```